New Business Card Design Project

Updated business card design. I am moving towards more coaching of, for the most part women, who are searching for more in their lives. I am an intuitive healer, homeopath and nutritionist but also an author and motivational speaker. Int the past I have included my photo on the card but that is not essential. My book is called the Brilliance of Saffron - Reclaiming the Shade of Your Spirit so my colours are typically magenta.
Target Market(s)
Women - 35 - 60 considering improving their health. However, I am also a professional speaker with a target audience including corporate and conferences.
Industry/Entity Type
Health And Wellness
Contact Information for Business Card
Delia Tranmoor, Hom, RHN, BA
www.deliatranmoor.example
delia@deliatranmoor.example
555-203-7914
Facebook, instagram and twitter logos
Look and feel
Each slider illustrates characteristics of the customer's brand and the style your logo design should communicate.

```html
<!DOCTYPE html>
<html lang="en">
<head>
<meta charset="utf-8">
<title>Delia Tranmoor — Business Card</title>
<link href="https://fonts.googleapis.com/css2?family=Roboto:wght@300;400;700&display=swap" rel="stylesheet">
<style>
  :root {
    --magenta: #ec1f8a;
    --magenta-soft: #f4a6cc;
    --ink: #3a3a3a;
    --paper: #fbfbfb;
    --stage: #e9e6e2;
    --photo-light: #f2efee;
    --photo-dark: #8c7468;
  }
  * { box-sizing: border-box; margin: 0; padding: 0; }
  html, body { width: 1200px; height: 886px; overflow: hidden; }
  body {
    background: var(--stage);
    font-family: "Roboto", Arial, sans-serif;
    display: flex;
    align-items: center;
    justify-content: center;
    gap: 40px;
  }
  .card {
    position: relative;
    width: 540px;
    height: 310px;
    background: var(--paper);
    box-shadow: 0 6px 18px rgba(0,0,0,0.18);
    overflow: hidden;
  }
  .card-front .portrait {
    position: absolute;
    top: 0;
    right: 0;
    width: 300px;
    height: 180px;
    background: radial-gradient(ellipse at 40% 45%, var(--photo-dark) 0%, #c9b7ae 45%, var(--photo-light) 80%);
  }
  .card-front .brand {
    position: absolute;
    left: 36px;
    top: 100px;
    display: flex;
    flex-direction: column;
    gap: 8px;
  }
  .brand-name {
    display: flex;
    align-items: center;
    gap: 8px;
    font-size: 26px;
    font-weight: 300;
    color: var(--ink);
  }
  .brand-dot {
    width: 18px;
    height: 18px;
    border-radius: 50%;
    background: var(--magenta);
  }
  .tagline {
    font-size: 13px;
    font-weight: 300;
    color: var(--ink);
    padding-left: 52px;
    letter-spacing: 0.5px;
  }
  .tagline span { color: var(--magenta); }
  .person {
    position: absolute;
    left: 190px;
    bottom: 46px;
  }
  .person-name {
    font-size: 17px;
    font-weight: 700;
    color: var(--magenta);
  }
  .person-credentials {
    font-size: 11px;
    color: var(--magenta);
    margin-top: 2px;
  }
  .contact-band {
    position: absolute;
    left: 0;
    right: 0;
    bottom: 10px;
    height: 22px;
    background: var(--magenta);
    color: #fff;
    font-size: 10.5px;
    display: flex;
    align-items: center;
    padding-left: 16px;
    gap: 10px;
  }
  .contact-band b { font-weight: 700; }
  .card-back {
    display: flex;
    align-items: center;
    justify-content: center;
  }
  .back-mark {
    display: flex;
    align-items: center;
    gap: 14px;
    font-size: 30px;
    font-weight: 300;
    color: var(--magenta);
  }
  .back-mark .brand-dot { width: 46px; height: 46px; }
</style>
</head>
<body>
  <section class="card card-front">
    <div class="portrait" role="img" aria-label="Portrait photograph of Delia Tranmoor in a white top"></div>
    <div class="brand">
      <div class="brand-name"><span class="brand-dot"></span>Delia Tranmoor</div>
      <div class="tagline"><span>•</span> wellness renegade <span>•</span></div>
    </div>
    <div class="person">
      <div class="person-name">Delia Tranmoor</div>
      <div class="person-credentials">Hom, RHN, BA</div>
    </div>
    <div class="contact-band">
      <span><b>P:</b> 555-203-7914</span>
      <span><b>E:</b> delia@deliatranmoor.example</span>
      <span><b>W:</b> www.deliatranmoor.example</span>
    </div>
  </section>
  <section class="card card-back">
    <div class="back-mark"><span class="brand-dot"></span>Delia Tranmoor</div>
  </section>
</body>
</html>
```